Corporate Power Point Template

Tarrowmead Group, Inc. produces and sells ready-mixed concrete, aggregates, and concrete-related products and services for the construction industry in the United States.

We are looking for a simple and sleek design that will look great on a projector, as well as when printed on paper. We prefer a lighter background color that will not waste ink when printed. We would also like to stay away from wavy banners, or over-the-top graphics that take away from usable space in the deck. Please use a variation of the color scheme in the "Brand Standards" file attached.

```html
<!DOCTYPE html>
<html lang="de">
<head>
<meta charset="utf-8">
<title>Tarrowmead Group – Slide Template</title>
<link href="https://fonts.googleapis.com/css2?family=Archivo:wght@800&family=Arimo:wght@400&display=swap" rel="stylesheet">
<style>
  :root {
    --bg: #ffffff;
    --rule: #7b7b7b;
    --edge: #8a8a8a;
    --text: #555555;
    --title: #000000;
    --brand: #5c6770;
    --accent: #d0202e;
    --footer: #262626;
    --footer-text: #c9c9c9;
    --pattern-a: #ffffff;
    --pattern-b: #eceaf0;
  }
  * { margin: 0; padding: 0; box-sizing: border-box; }
  html, body { width: 1200px; height: 675px; overflow: hidden; background: var(--bg); }
  .slide { position: relative; width: 1200px; height: 675px; background: var(--bg); overflow: hidden; font-family: "Arimo", Arial, sans-serif; }

  .texture { position: absolute; left: 28px; right: 28px; top: 420px; bottom: 25px;
    background: linear-gradient(to bottom, var(--pattern-a) 0%, var(--pattern-b) 100%); }

  .edge { position: absolute; top: 0; bottom: 25px; width: 26px; background: var(--edge); }
  .edge--left { left: 0; }
  .edge--right { right: 0; }

  .rule { position: absolute; width: 7px; background: var(--rule); }

  .brand { position: absolute; left: 91px; top: 20px; display: flex; align-items: center; gap: 8px; }
  .brand__mark { width: 14px; height: 14px; background: var(--accent); }
  .brand__name { font-family: "Arimo", Arial, sans-serif; font-size: 19px; line-height: 22px; color: var(--brand); letter-spacing: 0.5px; text-transform: uppercase; }

  .slide-title { position: absolute; left: 250px; top: 66px; font-family: "Archivo", Arial, sans-serif; font-weight: 800; font-size: 50px; line-height: 56px; color: var(--title); letter-spacing: -0.5px; }

  .column { position: absolute; top: 180px; list-style: none; }
  .column--left { left: 92px; width: 470px; }
  .column--right { left: 594px; width: 480px; }
  .column li { position: relative; padding-left: 22px; font-size: 30px; line-height: 32px; color: var(--text); margin-bottom: 11px; }
  .column li::before { content: "•"; position: absolute; left: 0; top: 0; font-size: 24px; color: var(--text); }

  .footer { position: absolute; left: 0; right: 0; bottom: 0; height: 25px; background: var(--footer); color: var(--footer-text); font-size: 12px; line-height: 25px; }
  .footer__tagline { position: absolute; left: 0; right: 0; text-align: center; }
  .footer__date { position: absolute; right: 40px; }
</style>
</head>
<body>
<div class="slide">
  <div class="texture" role="img" aria-label="Soft tiled square pattern fading in from the lower part of the slide"></div>

  <div class="edge edge--left"></div>
  <div class="edge edge--right"></div>

  <div class="rule" style="left:53px; top:0; bottom:25px;"></div>
  <div class="rule" style="left:66px; top:0; bottom:25px;"></div>
  <div class="rule" style="left:1095px; top:0; height:530px;"></div>
  <div class="rule" style="left:1114px; top:145px; height:385px;"></div>
  <div class="rule" style="left:1132px; top:0; height:413px;"></div>
  <div class="rule" style="left:1151px; top:262px; bottom:25px;"></div>

  <div class="brand">
    <span class="brand__mark"></span>
    <span class="brand__name">Tarrowmead<br>Group, Inc.</span>
  </div>

  <h1 class="slide-title">Click to add Slide Title</h1>

  <ul class="column column--left">
    <li>Wilde schmilzt blieb perlet du jedoch lange.</li>
    <li>Heimat herzen ist mich die gestehe denkst heut kleinem.</li>
    <li>Ergötzt träume. Ward mich nacht stund' liebe.</li>
    <li>Darfst komm ward stillestehn beiden dich lieb ein du.</li>
  </ul>

  <ul class="column column--right">
    <li>Seufzer von muß mein gut es schaust der. Werden gehn schmilzt die.</li>
    <li>Treibt glück im mut ruft heimat laue. In der sie dich du.</li>
    <li>Mal geschaut der manchmal einz'ges deine.</li>
    <li>Stürmten von der denkst weiter du sie ja.</li>
    <li>Wie friedlich gar. Weiter die stund' glück wärest geschaut du bist und.</li>
  </ul>

  <footer class="footer">
    <span class="footer__tagline">A TARROWMEAD GROUP COMPANY</span>
    <span class="footer__date">6/2/2017</span>
  </footer>
</div>
</body>
</html>
```